Brit Rock covers band "The Tin Kettles" requires poster for Marlowe Lounge Friday March 31st

I want a design for a poster (A3 and A4) and Facebook/Instagram ads.
Primary focus is the band name logo "The Tin Kettles", style as in attached file, followed by tag "Old Skool Brit Rock".
Backdrop to be 60's psychedelic art.
Secondary focus is the venue "The Marlowe Lounge"
Supporting text to include:
- 27 Fenwick Road, Chatswood SYDNEY
- Friday 31st March 2023
- 7:00 pm until late
- Bar sales refreshments
- NO admission fee

```html
<!DOCTYPE html>
<html lang="en">
<head>
<meta charset="utf-8">
<title>The Tin Kettles – Old Skool Brit Rock at The Marlowe Lounge</title>
<link rel="stylesheet" href="https://fonts.googleapis.com/css2?family=Cinzel:wght@900&family=Comfortaa:wght@500&family=Lobster&display=swap">
<style>
  :root {
    --blue-deep: #0a2fe6;
    --blue-mid: #1e63ff;
    --blue-light: #3fa2ff;
    --navy: #061048;
    --ink: #0b0b18;
    --steel-dark: #34373d;
    --steel-mid: #6b7079;
    --steel-light: #b9bec6;
    --white: #ffffff;
  }
  * { margin: 0; padding: 0; box-sizing: border-box; }
  html, body { width: 849px; height: 1200px; overflow: hidden; background: var(--blue-deep); }
  .poster {
    position: relative;
    width: 849px;
    height: 1200px;
    overflow: hidden;
  }
  .backdrop {
    position: absolute;
    inset: 0;
    background:
      radial-gradient(ellipse at 20% 30%, var(--blue-light) 0%, transparent 45%),
      radial-gradient(ellipse at 85% 70%, var(--blue-light) 0%, transparent 40%),
      linear-gradient(160deg, var(--blue-mid) 0%, var(--blue-deep) 55%, var(--blue-mid) 100%);
  }
  .portrait {
    position: absolute;
    left: 130px;
    top: 240px;
    width: 640px;
    height: 710px;
  }
  .metal-text {
    font-family: "Cinzel", serif;
    font-weight: 900;
    color: var(--steel-mid);
    background: linear-gradient(180deg, var(--steel-light) 0%, var(--steel-mid) 45%, var(--steel-dark) 100%);
    -webkit-background-clip: text;
    background-clip: text;
    -webkit-text-fill-color: transparent;
    filter:
      drop-shadow(2px 0 0 var(--white))
      drop-shadow(-2px 0 0 var(--white))
      drop-shadow(0 2px 0 var(--white))
      drop-shadow(0 -2px 0 var(--white))
      drop-shadow(3px 4px 3px rgba(0, 0, 0, 0.75));
  }
  .band-name-line {
    position: absolute;
    left: 0;
    width: 849px;
    text-align: center;
    line-height: 1;
    transform-origin: center top;
  }
  .band-name-line--top { top: 30px; font-size: 98px; transform: scaleY(1.75); }
  .band-name-line--bottom { top: 196px; font-size: 100px; transform: scaleY(2.2); }
  .band-name-line span {
    display: inline-block;
  }
  .tagline {
    position: absolute;
    top: 470px;
    left: 0;
    width: 849px;
    text-align: center;
    line-height: 1;
  }
  .tagline span {
    display: inline-block;
    font-size: 58px;
    transform: scaleY(1.25);
    transform-origin: center top;
  }
  .venue {
    position: absolute;
    top: 818px;
    left: 0;
    width: 849px;
    text-align: center;
    font-family: "Lobster", cursive;
    font-weight: 400;
    font-size: 86px;
    line-height: 1.1;
    color: var(--white);
    text-shadow: 3px 3px 0 var(--ink), -3px -3px 0 var(--ink), 3px -3px 0 var(--ink), -3px 3px 0 var(--ink), 5px 6px 0 var(--ink);
  }
  .details {
    position: absolute;
    top: 944px;
    left: 90px;
    list-style: none;
    font-family: "Comfortaa", sans-serif;
    font-weight: 500;
    font-size: 29px;
    line-height: 43px;
    color: var(--white);
    text-shadow: 0 0 6px var(--navy), 0 0 3px var(--navy);
  }
  .details li::before { content: "- "; }
</style>
</head>
<body>
<main class="poster">
  <div class="backdrop" role="img" aria-label="Blue 1960s psychedelic swirling pattern backdrop"></div>

  <svg class="portrait" viewBox="0 0 640 710" role="img" aria-label="Halftone illustration of a 60s rock figure with curly hair and round tinted sunglasses">
    <defs>
      <radialGradient id="portraitTone" cx="50%" cy="58%" r="55%">
        <stop offset="0%" stop-color="#4a6cff"/>
        <stop offset="55%" stop-color="#1a2a9a"/>
        <stop offset="100%" stop-color="#0a1560"/>
      </radialGradient>
    </defs>
    <ellipse cx="320" cy="370" rx="316" ry="336" fill="url(#portraitTone)"/>
  </svg>

  <h1 class="band-name">
    <span class="band-name-line band-name-line--top"><span class="metal-text">THE TIN</span></span>
    <span class="band-name-line band-name-line--bottom"><span class="metal-text">KETTLES</span></span>
  </h1>

  <p class="tagline"><span class="metal-text">OLD SKOOL BRIT ROCK</span></p>

  <h2 class="venue">The Marlowe Lounge</h2>

  <ul class="details">
    <li>27 Fenwick Road, Chatswood SYDNEY</li>
    <li>Friday 31st March 2023</li>
    <li>7:00 pm until late</li>
    <li>Bar sales refreshments</li>
    <li>NO admission fee</li>
  </ul>
</main>
</body>
</html>
```